依頼詳細
シンプルでインテリジェンスなデザインを希望してます。
記載項目
名前、役職名、メールアドレス
会社名、住所、電話、HPのURL、会社ロゴ、sorami.jpのロゴ
希望イメージ
シンプル 複雑
単色 カラフル
暗い 明るい
日常 高級
遊び心 厳粛
未来的 伝統的
女性的 男性的
希望する色
青系、水色系
納品ファイル
• イラストレーター形式 (.ai)
• フォトショップ形式 (.psd)
• PNG形式 (.png)
補足説明
BeRuMoネットワークのHP https://www.berumo.ne.jp/
sorami.jp http://www.sorami.jp/
会社ロゴ、sorami.jpロゴファルを添付しましたのでご活用ください
希望イメージを「厳格」寄りにしてしまいましたが、
「遊び心」あるデザインにてお願いします。
■ 選んだ理由

色調バランスがよく、文字の配置もまとまりがあり気に入りました!

■ 提案者全員のお礼・コメント

どれも丁寧な作品ばかりで、最終的には好みの選択になりました。
また別の機会でもご協力よろしくお願いします。

```html
<!DOCTYPE html>
<html lang="ja">
<head>
<meta charset="utf-8">
<title>BeRuMoネットワーク 名刺</title>
<link href="https://fonts.googleapis.com/css2?family=Noto+Sans+JP:wght@400;500;700&family=Noto+Serif+JP:wght@400&display=swap" rel="stylesheet">
<style>
  :root {
    --backdrop: #9fb2c9;
    --card: #ffffff;
    --ink: #1f1f1f;
    --ink-soft: #333333;
    --sky-top: #cfe0ee;
    --sky-mid: #b7c9d8;
    --city: #8f9aa6;
    --accent: #2b6cb0;
    --white: #ffffff;
  }
  * { margin: 0; padding: 0; box-sizing: border-box; }
  html, body {
    width: 856px; height: 1200px; overflow: hidden;
    background: var(--backdrop);
    font-family: "Noto Sans JP", sans-serif;
    color: var(--ink);
  }
  .card {
    position: absolute; left: 114px; top: 42px;
    width: 628px; height: 1063px;
    background: var(--card);
  }
  .hero {
    position: absolute; left: 0; top: 0; width: 628px; height: 330px;
    background: linear-gradient(180deg, var(--sky-top) 0%, var(--sky-mid) 55%, var(--city) 100%);
  }
  .hero-logo {
    position: absolute; left: 28px; top: 112px;
    font-size: 34px; font-weight: 700; color: var(--ink-soft);
    letter-spacing: 1px; line-height: 1;
  }
  .hero-tagline {
    position: absolute; left: 156px; top: 160px;
    font-size: 24px; font-weight: 500; color: var(--white);
    letter-spacing: 1px;
  }
  .company {
    position: absolute; left: 0; top: 336px; width: 628px;
    text-align: center; font-size: 27px; font-weight: 500; letter-spacing: 1px;
  }
  .rule {
    position: absolute; left: 28px; top: 386px; width: 572px; height: 1px;
    background: #bdbdbd;
  }
  .title {
    position: absolute; left: 0; top: 402px; width: 628px;
    text-align: center; font-size: 21px;
  }
  .name {
    position: absolute; left: 0; top: 440px; width: 628px;
    text-align: center; font-size: 48px; font-weight: 500; letter-spacing: 12px;
  }
  .contact {
    position: absolute; left: 28px; top: 556px; width: 572px;
    font-size: 22px; line-height: 38px; color: var(--ink-soft);
  }
  .contact-row { display: flex; justify-content: space-between; }
  .poem {
    position: absolute; left: 0; top: 762px; width: 628px;
    text-align: center; font-family: "Noto Serif JP", serif;
    font-size: 23px; line-height: 50px; color: var(--ink-soft);
  }
  .partner {
    position: absolute; left: 28px; top: 946px;
    display: flex; align-items: center; gap: 10px;
    font-size: 28px; font-weight: 700; color: var(--ink);
  }
  .partner-mark {
    width: 30px; height: 30px; border-radius: 50%; background: var(--accent);
  }
  .search {
    position: absolute; left: 256px; top: 940px; width: 330px; height: 54px;
    border: 3px solid var(--ink); border-radius: 12px;
    display: flex; align-items: center; gap: 12px; padding-left: 14px;
    font-size: 22px; color: var(--ink-soft);
  }
</style>
</head>
<body>
  <div class="card">
    <div class="hero" role="img" aria-label="東京の街並みとタワーの写真"></div>
    <div class="hero-logo">BeRuMo</div>
    <div class="hero-tagline">未来をちょっとsoramiにする</div>

    <div class="company">株式会社BeRuMoネットワーク</div>
    <div class="rule"></div>
    <div class="title">代表取締役</div>
    <div class="name">高橋 一郎</div>

    <div class="contact">
      <div>〒160-0011</div>
      <div>東京都新宿区若葉町218 若葉ビル502</div>
      <div class="contact-row"><span>Tel. 03-1234-5678</span><span>Mail. info@berumo.ne.jp</span></div>
      <div>https://www.berumo.ne.jp</div>
    </div>

    <div class="poem">
      <div>明日、晴れたらここへ行こう</div>
      <div>明日、雨ならこれをしよう</div>
      <div>そんな未来の予定を晴れにする</div>
    </div>

    <div class="partner"><span class="partner-mark"></span>sorami.jp</div>
    <div class="search">
      <svg width="26" height="26" viewBox="0 0 26 26" aria-hidden="true">
        <circle cx="10.5" cy="10.5" r="7.5" fill="none" stroke="#1f1f1f" stroke-width="3"/>
        <line x1="16" y1="16" x2="23.5" y2="23.5" stroke="#1f1f1f" stroke-width="3.5" stroke-linecap="round"/>
      </svg>
      <span>http://www.sorami.jp/</span>
    </div>
  </div>
</body>
</html>
```